Bold, dynamic Brick paver/landscaping company flyer

I need a flyer of 11" long x 8.5" high advertising our brick paver installation service. I want it clean, elegant and bold. I tried to give a general idea of what i was looking for by creating a very poor version for you guys to begin with. That being said, i am no designer, which is why i need your help. You have complete artistic license, show me what you got! I will attach our logo, the photos i used in the mock up as well as the mock up of basic idea. I hate my fonts, i hate to colors of them, i hate the way the pictures overlap without any seperation, but i like the basic idea. Use your artistic vision and skill to transform into something with a flair that will leave my potential customers thinking i am the most upscale service in the area. Please dont hesitate to ask any questions.

all of this bieng said, if you have an awesome idea thats completely different, im not invested in this idea alone, i will consider all options equally. Thanks!

Target Market(s)

high end homes, wealthy clientle

Industry/Entity Type

Advertising

Requirements
Must have
• Must have the blank white box in the upper right corner of approximate size, doesnt have to be exact. the gopher should be removed as well. The text "local postal customer should be there at the bottom of the box.

Company Name, phone number and web address

I like the wording of the text in the upper left, but hate the look of it

```html
<!DOCTYPE html>
<html lang="en">
<head>
<meta charset="utf-8">
<title>Stonebrook Terrace Landscaping – Flyer</title>
<link href="https://fonts.googleapis.com/css2?family=Cormorant+Garamond:ital,wght@0,600;1,500&family=Montserrat:wght@500;600&family=Arimo:wght@500&display=swap" rel="stylesheet">
<style>
  :root {
    --forest: #132a1b;
    --forest-band: #1b3a25;
    --forest-shade: #0d1f13;
    --gold: #c9a45c;
    --gold-soft: #e2c88f;
    --cream: #f4efe4;
    --white: #ffffff;
    --ink: #111111;
    --photo-patio: linear-gradient(160deg, #2e2a26 0%, #5c4c3c 45%, #9a8468 100%);
    --photo-house: linear-gradient(180deg, #3d6fb0 0%, #5e86b8 55%, #8f8f86 100%);
    --photo-firepit: linear-gradient(180deg, #1c1f22 0%, #3a3b38 60%, #6a6455 100%);
    --photo-pool: linear-gradient(180deg, #8aa4c2 0%, #6c7d58 50%, #3f7a2c 100%);
    --photo-walk: linear-gradient(180deg, #9ab8d8 0%, #5f8a3a 45%, #8c6b4a 100%);
  }
  html, body {
    margin: 0;
    padding: 0;
    width: 1200px;
    height: 927px;
    overflow: hidden;
    background: var(--forest);
  }
  .flyer {
    position: relative;
    width: 1200px;
    height: 927px;
    overflow: hidden;
    background: var(--forest);
    font-family: "Cormorant Garamond", Garamond, serif;
    color: var(--cream);
  }
  .flyer__band {
    position: absolute;
    inset: 0;
  }

  /* Header */
  .brand {
    position: absolute;
    left: 64px;
    top: 48px;
  }
  .brand__name {
    margin: 0;
    font-weight: 600;
    font-size: 58px;
    line-height: 1;
    letter-spacing: 0.01em;
    color: var(--cream);
    white-space: nowrap;
  }
  .brand__rule {
    width: 120px;
    height: 2px;
    margin: 22px 0 18px;
    background: var(--gold);
  }
  .brand__web {
    margin: 0;
    font-family: "Montserrat", Arial, sans-serif;
    font-weight: 500;
    font-size: 17px;
    letter-spacing: 0.22em;
    text-transform: uppercase;
    color: var(--gold-soft);
    white-space: nowrap;
  }

  /* Mailing box */
  .postal-box {
    position: absolute;
    left: 992px;
    top: 20px;
    width: 188px;
    height: 185px;
    box-sizing: border-box;
    padding: 0 18px 16px;
    background: var(--white);
    display: flex;
    flex-direction: column;
    justify-content: flex-end;
    font-family: "Arimo", Arial, sans-serif;
    font-weight: 500;
    font-size: 22px;
    line-height: 27px;
    color: var(--ink);
  }

  /* Gallery */
  .gallery {
    position: absolute;
    left: 64px;
    top: 250px;
    width: 1072px;
    height: 380px;
    display: grid;
    grid-template-columns: 560px 1fr 1fr;
    grid-template-rows: 1fr 1fr;
    gap: 20px;
  }
  .photo {
    box-sizing: border-box;
    border: 6px solid var(--cream);
    box-shadow: 0 0 0 1px var(--gold), 0 10px 24px rgba(0, 0, 0, 0.45);
  }
  .photo--patio { grid-row: 1 / span 2; background: var(--photo-patio); }
  .photo--house { background: var(--photo-house); }
  .photo--firepit { background: var(--photo-firepit); }
  .photo--pool { background: var(--photo-pool); }
  .photo--walk { background: var(--photo-walk); }

  /* Tagline */
  .tagline {
    position: absolute;
    left: 64px;
    top: 676px;
    margin: 0;
    font-style: italic;
    font-weight: 500;
    font-size: 46px;
    line-height: 56px;
    white-space: nowrap;
  }
  .tagline__lead { display: block; color: var(--cream); }
  .tagline__close { display: block; padding-left: 48px; color: var(--gold); }

  /* Contact */
  .contact {
    position: absolute;
    right: 64px;
    top: 820px;
    display: flex;
    align-items: center;
    gap: 16px;
  }
  .contact__icon {
    width: 44px;
    height: 44px;
  }
  .contact__phone {
    margin: 0;
    font-weight: 600;
    font-size: 50px;
    line-height: 1;
    letter-spacing: 0.02em;
    color: var(--gold);
    white-space: nowrap;
  }
  .footer-rule {
    position: absolute;
    left: 64px;
    right: 64px;
    top: 800px;
    height: 1px;
    background: var(--gold);
    opacity: 0.6;
  }
</style>
</head>
<body>
<main class="flyer">
  <svg class="flyer__band" width="1200" height="927" viewBox="0 0 1200 927" aria-hidden="true">
    <polygon points="60,0 600,0 1200,740 1200,927 680,927" fill="var(--forest-band)"/>
    <line x1="600" y1="0" x2="1200" y2="740" stroke="var(--gold)" stroke-width="1" opacity="0.35"/>
  </svg>

  <header class="brand">
    <h1 class="brand__name">Stonebrook Terrace Landscaping</h1>
    <div class="brand__rule"></div>
    <p class="brand__web">www.StonebrookTerrace.com</p>
  </header>

  <div class="postal-box">Local<br>Postal<br>Customer</div>

  <section class="gallery">
    <div class="photo photo--patio" role="img" aria-label="Photo of a curved brick paver patio at dusk with a stone fireplace and outdoor dining set"></div>
    <div class="photo photo--house" role="img" aria-label="Photo of a lit modern home with a paver pool deck at twilight"></div>
    <div class="photo photo--firepit" role="img" aria-label="Photo of a paver patio at night with lounge chairs around a glowing fire pit"></div>
    <div class="photo photo--pool" role="img" aria-label="Photo of a landscaped backyard with lawn, pavers and a pool"></div>
    <div class="photo photo--walk" role="img" aria-label="Photo of a curved paver walkway with mulched garden beds beside a pool"></div>
  </section>

  <p class="tagline">
    <span class="tagline__lead">Where the elegance of pavers…</span>
    <span class="tagline__close">meets the beauty of design.</span>
  </p>

  <div class="footer-rule"></div>

  <div class="contact">
    <svg class="contact__icon" viewBox="0 0 24 24" aria-hidden="true">
      <path d="M6.6 10.8a15.1 15.1 0 0 0 6.6 6.6l2.2-2.2a1 1 0 0 1 1-.25 11.4 11.4 0 0 0 3.6.57 1 1 0 0 1 1 1V20a1 1 0 0 1-1 1A17 17 0 0 1 3 4a1 1 0 0 1 1-1h3.5a1 1 0 0 1 1 1c0 1.25.2 2.45.57 3.6a1 1 0 0 1-.25 1z" fill="var(--gold)"/>
    </svg>
    <p class="contact__phone">(555) 218-4630</p>
  </div>
</main>
</body>
</html>
```